Flyer Design Project

Painting and Maintenance
This is what I have as idea as Job description
Refresh, renew & revive your home. from painting to carpentry. Do you guys have any epic unique slogan?
As what we do Residential - Commercial Interior - ExteriorTrim & Molding installationWainscoting - Wallpaper removalCabinet refinishing Woodwork EnamelingDeck & Fence Cleaning & SealingPressure washConcrete & Paver Washing
I would like to have a note that says-Prompt professional service-Free estimates-Insured -"visit us on PalPorch"
I would like new ideas from you guys as well!
Carpentry

```html
<!DOCTYPE html>
<html lang="en">
<head>
<meta charset="utf-8">
<title>Hollbrook Painting &amp; Maintenance Flyer</title>
<link rel="stylesheet" href="https://fonts.googleapis.com/css2?family=Archivo+Black&family=Cabin:wght@500&family=Roboto:ital,wght@0,700;1,900&display=swap">
<style>
  :root{
    --red:#d40f0f;
    --red-dark:#b30c0c;
    --charcoal:#46474b;
    --ink:#3a3a3d;
    --white:#ffffff;
    --backdrop:#e4e4e4;
  }
  *{box-sizing:border-box;margin:0;padding:0}
  html,body{width:1200px;height:1200px;overflow:hidden;background:var(--backdrop)}
  .flyer{
    position:absolute;left:225px;top:30px;width:852px;height:1295px;
    transform:scale(.88);transform-origin:top left;
    background:var(--white);overflow:hidden;
    box-shadow:0 6px 18px rgba(0,0,0,.25);
  }
  .abs{position:absolute}
  .header{left:0;top:0;width:852px;height:245px;background:linear-gradient(180deg,var(--red),var(--red-dark));
    color:var(--white);text-align:center;font-family:"Archivo Black",sans-serif}
  .header .line1{position:absolute;top:34px;width:100%;font-size:47px;letter-spacing:1px}
  .header .line2{position:absolute;top:91px;width:100%;font-size:47px;letter-spacing:1px}
  .header .line3{position:absolute;top:148px;width:100%;font-size:36px;letter-spacing:1px}
  .rule-dark{left:0;top:246px;width:852px;height:4px;background:var(--charcoal)}
  .rule-red{left:0;top:253px;width:852px;height:3px;background:var(--red)}
  .hero{left:0;top:258px;width:852px;height:470px;
    background:linear-gradient(180deg,#d9dde6 0%,#b9bfcc 28%,#8c8f98 48%,#c9ab84 64%,#8a7a6a 80%,#5f8a3c 92%,#4c7a2e 100%)}
  .brand{left:26px;top:262px;font-family:"Archivo Black",sans-serif;color:var(--ink);line-height:1}
  .brand .name{font-size:50px;letter-spacing:1px}
  .brand .name2{font-size:44px;margin-top:4px;letter-spacing:1px}
  .brand .tag{font-size:17px;margin-top:8px;letter-spacing:2px}
  .photo{top:729px;width:267px;height:180px;border:3px solid var(--white)}
  .photo-1{left:16px;background:linear-gradient(160deg,#e8eef2,#9aa3ad 45%,#c9b98f 70%,#6f8d4a)}
  .photo-2{left:295px;background:linear-gradient(90deg,#9c7650,#c8c9cb 30%,#b8b6b2 50%,#d9d7d2 70%,#a9a7a3)}
  .photo-3{left:573px;background:linear-gradient(180deg,#5a8f3a 0%,#6b9a45 25%,#8c8f99 45%,#6c7079 100%)}
  .services{left:0;top:882px;width:852px;height:183px;background:var(--charcoal)}
  .list{position:absolute;top:40px;list-style:none;font-family:"Cabin",sans-serif;font-size:21.5px;color:var(--white)}
  .list li{position:relative;padding-left:22px;line-height:25px;margin-bottom:8px;white-space:nowrap}
  .list svg{position:absolute;left:0;top:5px}
  .list-1{left:16px}
  .list-2{left:304px}
  .list-3{left:585px}
  .list-3 li{margin-bottom:12px}
  .divider{position:absolute;top:48px;width:2px;height:118px;background:#cfcfcf}
  .contact{left:0;top:1068px;width:852px;height:52px;background:var(--red);color:var(--white);
    font-family:"Roboto",sans-serif;font-weight:700;font-size:22px}
  .contact span,.contact svg{position:absolute;top:13px}
  .notes{font-family:"Roboto",sans-serif;font-style:italic;font-weight:900;color:var(--red);font-size:29px;line-height:35px;white-space:nowrap}
  .splat{width:50px;height:50px;border-radius:50%;background:#58595d}
  .brush-art{left:18px;top:1210px;width:116px;height:76px;
    background:linear-gradient(135deg,#6a6b70 0%,#8a8b90 50%,#c43a3a 100%)}
  .social{left:100px;top:1219px;width:752px;height:60px;background:var(--red);
    clip-path:polygon(0 0,100% 0,100% 100%,6% 100%,3% 60%);
    font-family:"Cabin",sans-serif;font-size:24px;color:var(--white)}
  .social .mark{position:absolute;left:58px;top:18px;width:25px;height:25px;background:#3d5ea0}
  .social .txt{position:absolute;left:103px;top:15px;white-space:nowrap}
</style>
</head>
<body>
<div class="flyer">
  <div class="abs header">
    <div class="line1">REFRESH, RENEW &amp; REVIVE</div>
    <div class="line2">YOUR HOME</div>
    <div class="line3">FROM PAINTING TO CARPENTRY</div>
  </div>
  <div class="abs rule-dark"></div>
  <div class="abs rule-red"></div>

  <div class="abs hero" role="img" aria-label="Photo of a large two-storey grey-shingled house at dusk with lit windows, garage doors and a green lawn"></div>

  <div class="abs brand">
    <div class="name">HOLLBROOK</div>
    <div class="name2">PAINTING</div>
    <div class="tag">&amp; MAINTENANCE LLC.</div>
  </div>

  <div class="abs photo photo-1" role="img" aria-label="Photo of a painter on a ladder working on house exterior trim"></div>
  <div class="abs photo photo-2" role="img" aria-label="Before and after photo of refinished kitchen cabinets around wall ovens"></div>
  <div class="abs photo photo-3" role="img" aria-label="Photo of pavers being sealed with a roller"></div>

  <div class="abs services">
    <svg width="0" height="0" style="position:absolute">
      <defs>
        <symbol id="tick" viewBox="0 0 16 16">
          <rect x="1" y="3" width="11" height="11" fill="none" stroke="#fff" stroke-width="1.6"/>
          <path d="M3.5 8.5l3 3L15 2" fill="none" stroke="#fff" stroke-width="2.4"/>
        </symbol>
      </defs>
    </svg>
    <ul class="list list-1">
      <li><svg width="16" height="16"><use href="#tick"/></svg>Residential - Commercial</li>
      <li><svg width="16" height="16"><use href="#tick"/></svg>Interior - Exterior</li>
      <li><svg width="16" height="16"><use href="#tick"/></svg>Trim &amp; Molding Installation</li>
      <li><svg width="16" height="16"><use href="#tick"/></svg>Drywall Repair</li>
    </ul>
    <div class="divider" style="left:292px"></div>
    <ul class="list list-2">
      <li><svg width="16" height="16"><use href="#tick"/></svg>Wainscoting &amp; Wallpaper<br>Removal</li>
      <li><svg width="16" height="16"><use href="#tick"/></svg>Cabinet Refinishing</li>
      <li><svg width="16" height="16"><use href="#tick"/></svg>Woodwork Enameling</li>
    </ul>
    <div class="divider" style="left:570px"></div>
    <ul class="list list-3">
      <li><svg width="16" height="16"><use href="#tick"/></svg>Deck &amp; Fence Sealing</li>
      <li><svg width="16" height="16"><use href="#tick"/></svg>Concrete &amp; Paver Sealing</li>
      <li><svg width="16" height="16"><use href="#tick"/></svg>Pressure Wash</li>
    </ul>
  </div>

  <div class="abs contact">
    <span style="left:30px">Contact Us today!</span>
    <svg style="left:266px" width="28" height="28" viewBox="0 0 28 28">
      <circle cx="14" cy="14" r="12.5" fill="none" stroke="#fff" stroke-width="2"/>
      <path d="M9 7.5l3 3-1.6 2c1 2 2.5 3.6 4.4 4.5l2-1.7 3 3-1.8 2.2C12.5 20 8 15.4 7 9.2z" fill="#fff"/>
    </svg>
    <span style="left:304px">5550148822</span>
    <svg style="left:479px" width="28" height="28" viewBox="0 0 28 28">
      <circle cx="14" cy="14" r="12.5" fill="none" stroke="#fff" stroke-width="2"/>
      <rect x="7.5" y="9.5" width="13" height="9" fill="none" stroke="#fff" stroke-width="1.8"/>
      <path d="M7.5 9.5l6.5 5 6.5-5" fill="none" stroke="#fff" stroke-width="1.8"/>
    </svg>
    <span style="left:514px">hollbrook_paint@mailbox.com</span>
  </div>

  <div class="abs splat" style="left:16px;top:1140px" role="img" aria-label="Grey paint splash icon"></div>
  <div class="abs notes" style="left:81px;top:1133px">PROMPT PROFESSIONAL<br>SERVICE</div>
  <div class="abs splat" style="left:456px;top:1140px" role="img" aria-label="Grey paint splash icon"></div>
  <div class="abs notes" style="left:531px;top:1133px">FREE ESTIMATES<br>INSURED</div>

  <div class="abs social">
    <div class="mark"></div>
    <div class="txt">Visit us on PalPorch : /Hollbrook-Painting-Maintenance-LLC</div>
  </div>
  <div class="abs brush-art" role="img" aria-label="Illustration of a paintbrush with red paint"></div>
</div>
</body>
</html>
```